Wholesale food company needs a package for Carp boilies (fishing)

We need a (5kg) doypack with handle design for a new brand here in the BENELUX called Vornel Lures. We already have a logo but we need a flashing design to promote it on shows and webshops. The design must also include some transparant places so you can see the product inside. We have added the logo and the website is www.vornellures.nl. You can look for an impression at http://kestamo-goods.nl/product-category/baits/specials/

Target Market(s)

Carpf fishing and coarse angling

Industry/Entity Type

It Company

Requirements
Must have
• A slogan that suits both types of fishing.
• Extra information doypack:
• Material: PET/PE
• Thickness: 12µ/120µ
• Size: B 320 x H 450 MM

```html
<!DOCTYPE html>
<html lang="en">
<head>
<meta charset="utf-8">
<title>Vornel Lures – Boilies Doypack</title>
<link rel="stylesheet" href="https://fonts.googleapis.com/css2?family=Montserrat:wght@500;700&family=Oswald:wght@700&family=Roboto+Condensed:ital,wght@1,500&display=swap">
<style>
  :root {
    --backdrop: #cfcfcf;
    --pouch-white: #f2f2f2;
    --brand-green: #7cc242;
    --brand-blue: #1b3a9c;
    --title-blue: #1e6fd0;
    --text-dark: #1a1a1a;
    --boilie-red: #b3262f;
    --boilie-deep: #7e1219;
    --boilie-light: #d9616a;
  }
  * { margin: 0; padding: 0; box-sizing: border-box; }
  html, body { width: 1200px; height: 900px; overflow: hidden; }
  body { background: var(--backdrop); position: relative; font-family: "Montserrat", sans-serif; }

  .pouch { position: absolute; left: 345px; top: 70px; width: 510px; height: 755px; overflow: hidden; }
  .pouch-shape { position: absolute; inset: 0; }

  .sticker-row { position: absolute; top: 18px; left: 0; width: 510px; display: flex; justify-content: space-around; padding: 0 20px; }
  .sticker { width: 70px; height: 70px; border-radius: 50%; background: #fff; border: 2px solid #dfe8d6;
    display: flex; align-items: center; justify-content: center; text-align: center;
    font-weight: 700; font-size: 11px; line-height: 1.1; color: var(--brand-blue); }

  .brand-seal { position: absolute; left: 18px; top: 128px; width: 210px; height: 210px; border-radius: 50%;
    border: 5px solid var(--brand-green); background: #fff;
    display: flex; align-items: center; justify-content: center; text-align: center;
    font-weight: 700; font-size: 30px; line-height: 1.1; color: var(--title-blue); }

  .product-name { position: absolute; left: 258px; top: 142px; width: 240px; font-family: "Oswald", sans-serif; font-style: italic;
    font-weight: 700; font-size: 33px; line-height: 1.15; letter-spacing: -0.3px; color: var(--title-blue); white-space: nowrap;
    text-shadow: 2px 2px 0 var(--brand-blue); }

  .benefits { position: absolute; left: 262px; top: 203px; width: 240px; list-style: none; }
  .benefits li { position: relative; padding-left: 16px; font-weight: 500; font-size: 15px; line-height: 1.2; color: var(--text-dark); margin-bottom: 8px; white-space: nowrap; }
  .benefits li::before { content: ""; position: absolute; left: 1px; top: 6px; width: 7px; height: 7px; border-radius: 50%; background: var(--brand-green); }

  .blurb { position: absolute; left: 264px; top: 292px; width: 232px; font-family: "Roboto Condensed", sans-serif;
    font-style: italic; font-weight: 500; font-size: 10.5px; line-height: 1.25; color: var(--text-dark); }

  .website { position: absolute; left: 0; width: 510px; top: 697px; text-align: center; font-weight: 700; font-size: 17px; letter-spacing: 1px; color: var(--text-dark); }
</style>
</head>
<body>
  <div class="pouch">
    <svg class="pouch-shape" viewBox="0 0 510 755" width="510" height="755">
      <defs>
        <radialGradient id="boilie-fill" cx="50%" cy="45%" r="70%">
          <stop offset="0" stop-color="var(--boilie-light)"/>
          <stop offset="0.55" stop-color="var(--boilie-red)"/>
          <stop offset="1" stop-color="var(--boilie-deep)"/>
        </radialGradient>
      </defs>
      <rect x="0" y="0" width="510" height="755" rx="6" fill="var(--pouch-white)"/>
      <rect class="top-band" x="0" y="0" width="510" height="100" fill="var(--brand-green)"/>
      <rect x="0" y="100" width="510" height="7" fill="var(--brand-blue)"/>
      <path class="window" role="img" aria-label="Transparent window showing red boilies inside"
        d="M10 368 Q255 395 500 362 L500 615 Q255 612 10 632 Z" fill="url(#boilie-fill)"/>
      <path d="M0 345 Q255 375 510 340" fill="none" stroke="var(--brand-blue)" stroke-width="9"/>
      <path d="M0 356 Q255 386 510 351" fill="none" stroke="var(--brand-green)" stroke-width="7"/>
      <path d="M0 635 Q255 612 510 613" fill="none" stroke="var(--brand-green)" stroke-width="7"/>
      <path d="M0 646 Q255 624 510 625" fill="none" stroke="var(--brand-blue)" stroke-width="9"/>
    </svg>

    <div class="sticker-row">
      <div class="sticker">Vornel Lures</div>
      <div class="sticker">Vornel Lures</div>
      <div class="sticker">Vornel Lures</div>
      <div class="sticker">Vornel Lures</div>
      <div class="sticker">Vornel Lures</div>
    </div>

    <div class="brand-seal">Vornel<br>Lures</div>

    <h1 class="product-name">PRODUCT NAME</h1>
    <ul class="benefits">
      <li>Lorem ipsum dolor sit amet</li>
      <li>Consectetur adipisicing elit</li>
      <li>Quis nostrud exercitation</li>
    </ul>
    <p class="blurb">Lorem ipsum dolor sit amet, consectetur adipisicing elit, sed do eiusmod tempor incididunt ut labore et dolore magna aliqua. Ut enim ad minim veniam, quis nostrud exercitation.</p>

    <p class="website">WWW.VORNELLURES.NL</p>
  </div>
</body>
</html>
```